MUSIC FESTIVAL 2023

On the occasion of the 2023 music festival, the Le Trente, brings the VENTOLIRE group to its terrace.
We are organizing a giant barbecue on this occasion.
This event is organized in collaboration with LE MORVAN.
Possibility of take-out!
Address of the event: 12-16 Place Gaston Morlier in CAMBRAI.4
From 19h.
03 41 56 92 17 - lucas@ormeval-gestione.com
Please write in French.
To use the logos of the two establishments.

```html
<!DOCTYPE html>
<html lang="fr">
<head>
<meta charset="utf-8">
<title>Fête de la musique 2023 – Affiche</title>
<link rel="stylesheet" href="https://fonts.googleapis.com/css2?family=Anton&family=Montserrat:ital,wght@0,400;0,600;0,700;0,800;1,700;1,800&display=swap">
<style>
  :root{
    --page:#e9e6e2;
    --black:#0b0b0b;
    --white:#ffffff;
    --gold:#c8962e;
    --slate:#4d6b7f;
    --food-a:#b98a5c;
    --food-b:#6e4a3a;
    --veg-a:#9b2b4e;
    --veg-b:#2a1d22;
    --steel-a:#8a8a8a;
    --steel-b:#3c3c3c;
    --cafe-a:#c9cfd6;
    --cafe-b:#6f7f8f;
  }
  *{box-sizing:border-box;margin:0;padding:0}
  html,body{width:1200px;height:800px;overflow:hidden}
  body{background:var(--page);font-family:"Montserrat",sans-serif}
  .flyer{position:absolute;left:330px;top:18px;width:540px;height:764px;background:var(--black);overflow:hidden;box-shadow:0 6px 24px rgba(0,0,0,.25)}
  .photo{position:absolute}
  .photo-buffet{left:200px;top:0;width:340px;height:262px;background:linear-gradient(135deg,var(--food-a),var(--food-b))}
  .photo-platter{left:0;top:70px;width:200px;height:220px;background:linear-gradient(160deg,var(--veg-b),var(--veg-a))}
  .photo-instruments{left:318px;top:262px;width:222px;height:300px;background:linear-gradient(150deg,var(--steel-a),var(--steel-b))}
  .photo-cafe{left:18px;top:608px;width:504px;height:104px;background:linear-gradient(110deg,var(--cafe-b),var(--cafe-a))}
  .band-slate{position:absolute;left:0;top:596px;width:540px;height:126px;background:var(--slate)}
  .host-mark{position:absolute;left:222px;top:112px;display:flex;align-items:center;gap:10px}
  .host-mark .dot{width:22px;height:22px;border-radius:50%;background:var(--white)}
  .host-mark .name{font-weight:700;font-size:24px;color:var(--white);line-height:1}
  .band-name{position:absolute;left:250px;top:562px;transform-origin:0 0;transform:rotate(-90deg);font-family:"Anton",sans-serif;font-size:64px;line-height:64px;color:var(--white);letter-spacing:1px;width:300px;text-align:center;white-space:nowrap}
  .intro{position:absolute;left:22px;top:300px;width:222px;color:var(--white)}
  .intro p{font-size:12.5px;line-height:1.3;margin-bottom:10px;font-weight:600}
  .highlight{display:inline-block;background:var(--gold);color:var(--black);font-weight:800;font-style:italic;padding:1px 5px;margin:2px 0}
  .italic-bold{font-style:italic;font-weight:700}
  .gold{color:var(--gold)}
  .rule{height:1px;background:var(--gold);width:200px;margin:6px 0 12px}
  .intro .takeout{font-style:italic;font-weight:800;font-size:13px}
  .intro .address-title{color:var(--gold);font-weight:800;font-size:12.5px;margin:6px 0 4px}
  .intro .address{font-weight:400;font-size:12.5px;line-height:1.35}
  .partner-mark{position:absolute;left:0;top:632px;width:540px;text-align:center;color:var(--black)}
  .partner-mark .name{font-weight:700;font-size:30px;line-height:1}
  .partner-mark .sub{font-weight:700;font-size:12px;letter-spacing:3px;margin-top:6px}
  .contact{position:absolute;left:0;top:722px;width:540px;height:42px;display:flex;justify-content:center;align-items:center;gap:28px;color:var(--white);font-size:12px}
  .contact span{display:flex;align-items:center;gap:6px}
</style>
</head>
<body>
<main class="flyer">
  <div class="photo photo-buffet" role="img" aria-label="Buffet de burgers au sésame et de charcuterie"></div>
  <div class="photo photo-platter" role="img" aria-label="Bouteille de champagne, plateau de légumes et nachos"></div>
  <div class="host-mark"><span class="dot"></span><span class="name">Le Trente</span></div>

  <div class="photo photo-instruments" role="img" aria-label="Photo noir et blanc de guitares, micro et baguettes sur un parquet"></div>
  <h1 class="band-name">VENTOLIRE</h1>

  <section class="intro">
    <p>À l'occasion de la<br>
      <span class="highlight">FÊTE DE LA MUSIQUE 2023</span><br>
      <span class="italic-bold">Le Trente accueille le groupe<br>VENTOLIRE sur sa terrasse</span></p>
    <div class="rule"></div>
    <p>Nous organisons un<br><span class="gold">barbecue géant pour l'occasion</span></p>
    <p>Cet événement est organisé en<br><span class="gold">collaboration avec LE MORVAN.</span></p>
    <p class="takeout">Possibilité de vente à emporter !</p>
    <p class="address-title">ADRESSE DE L'ÉVÉNEMENT :</p>
    <p class="address">12-16 Place Gaston Morlier<br>à CAMBRAI.4 dès 19h.</p>
  </section>

  <div class="band-slate"></div>
  <div class="photo photo-cafe" role="img" aria-label="Intérieur du café-brasserie avec banquettes et suspensions"></div>
  <div class="partner-mark">
    <div class="name">Le Morvan</div>
    <div class="sub">CAFÉ - BRASSERIE</div>
  </div>

  <footer class="contact">
    <span><svg width="14" height="14" viewBox="0 0 14 14"><circle cx="7" cy="7" r="6" fill="none" stroke="var(--gold)" stroke-width="1.4"/><path d="M4.5 4.2l1.3-.2.6 1.5-.8.6a4 4 0 0 0 2.3 2.3l.6-.8 1.5.6-.2 1.3c-3 .2-5.5-2.3-5.3-5.3z" fill="var(--gold)"/></svg>03 41 56 92 17</span>
    <span><svg width="14" height="14" viewBox="0 0 14 14"><circle cx="7" cy="7" r="6" fill="none" stroke="var(--gold)" stroke-width="1.4"/><rect x="3.8" y="4.8" width="6.4" height="4.4" fill="none" stroke="var(--gold)" stroke-width="1"/><path d="M3.8 4.8L7 7.4l3.2-2.6" fill="none" stroke="var(--gold)" stroke-width="1"/></svg>lucas@ormeval-gestione.com</span>
  </footer>
</main>
</body>
</html>
```